Real Estate Development and Brokerage Middle East

Required is a web site design for a new branch of an existing Real Estate Development and Brokerage company. The Branch will be established in the United Arab Emirates - Corvalis Middle East, the mother company is based in Austria/Europe. The new branch focuses on the middle eastern clients such as Institutional Investors/Family Businesses/Wealthy Individuals looking either for a luxury home in Vienna City or the alpine nature or are interested to invest in ready made properties or real estate development projects in Austria run by the branches mother co. in Austria. The design should highlight both Services i.e. Investment for commercial purpose and for residential purposes (focus on the nature) as well as the companies focus on high end luxury selected properties only and having middle east experienced staff in the UAE.

The link to the Austrian HQ website is below: Design elements of that website might or might not be used, however the logo shall be the same.
http://brindlemock.example/QW7ZTRXLM

Attached the logo and a rough first draft of the structure of the website (not yet set in stone) . The attachment contains also a link to a website of a company in a similar industry. I do like the way they present the highlights on their start/home page. The boxes. By the way, we believe that more graphic (pictures) and a bit less text might be a good way to approach our future target customers.

As we hope to sell many of the projects and hence many new projects descriptions/pictures will be uploaded in future on an ongoing basis the page should have the ability to upload information and pics by our team (none of it is a web designer and has experience exceeding MS-Office).

Lastly - and for the future we might need (not sure yet) need the entire context in Arabic (the language button)

Thanks.
Olaf

Target Market(s)

Institutional Investors and wealthy individuals / family offices

Industry/Entity Type

Real Estate

Coding

Number of Pages Required

Requirements
Must have
• Same Logo as Parent Company
Nice to have
• News ticker/banner, high resolution picture heavy, changing pictures on start/home page, PDF downloads

```html
<!DOCTYPE html>
<html lang="en">
<head>
<meta charset="utf-8">
<title>Corvalis Immobilien – Real Estate Development and Brokerage</title>
<link rel="stylesheet" href="https://fonts.googleapis.com/css2?family=Teko:wght@400;500&family=Open+Sans:wght@400;600&family=Arimo:wght@400;700&display=swap">
<style>
:root{
  --ink:#2b2b2b;
  --text:#444;
  --muted:#777;
  --sky:#b9d4e2;
  --card-bottom:#4b6d85;
  --footer:#5e87a5;
  --footer-rim:#c9d3da;
  --grey-band:#e6e6e6;
  --accent-red:#a31d1d;
  --link-blue:#1f4fa8;
  --white:#fff;
}
*{margin:0;padding:0;box-sizing:border-box}
html,body{width:714px;height:1200px;overflow:hidden;background:var(--white)}
body{position:relative;font-family:"Arimo",Arial,sans-serif;color:var(--text)}
.abs{position:absolute}

/* header */
.site-header{position:absolute;left:0;top:0;width:714px;height:74px;background:var(--white)}
.brand{position:absolute;left:62px;top:38px;display:flex;align-items:center;gap:6px}
.brand-mark{width:12px;height:12px;background:#5b8fb6}
.brand-name{font-family:"Arimo",sans-serif;font-size:15px;font-weight:400;color:#1e1e1e;letter-spacing:.2px}
.main-nav{position:absolute;top:38px;left:222px;display:flex}
.main-nav a{font-family:"Open Sans",sans-serif;font-size:9.6px;color:#222;text-decoration:none;height:19px;line-height:18px;padding:0 6px;margin-right:15px}
.main-nav a.is-current{border:1px solid #5a7d95}

/* hero */
.hero{position:absolute;left:0;top:74px;width:714px;height:316px;background:linear-gradient(160deg,#3e5b7c 0%,#6f8fb3 35%,#c9d6e4 60%,#7f9ab8 80%,#3f5674 100%)}
.hero-caption{position:absolute;left:60px;top:119px;width:350px;height:52px;background:rgba(20,24,30,.78);padding:8px 10px}
.hero-caption h1{font-family:"Teko",sans-serif;font-weight:400;font-size:22px;line-height:22px;color:var(--white)}
.hero-caption p{font-family:"Arimo",sans-serif;font-size:8.5px;color:var(--white);margin-top:3px}

/* audience band */
.audience-band{position:absolute;left:0;top:390px;width:714px;height:193px;background:var(--sky)}
.audience-card{position:absolute;top:357px;width:178px;height:198px;background:linear-gradient(180deg,rgba(111,151,178,.92),var(--card-bottom))}
.audience-card h2{font-family:"Teko",sans-serif;font-weight:400;font-size:19px;color:var(--white);text-align:center;height:32px;line-height:34px;border-bottom:1px dashed rgba(255,255,255,.35)}
.audience-card .thumb{position:absolute;left:8px;top:41px;width:162px;height:80px;border:2px solid var(--white)}
.audience-card p{position:absolute;left:8px;top:129px;width:166px;font-family:"Open Sans",sans-serif;font-size:7.6px;line-height:12px;color:var(--white)}

/* media section */
.section-title{font-family:"Arimo",sans-serif;font-weight:400;font-size:16px;color:#222;letter-spacing:.3px}
.rule-dashed{height:0;border-top:1px dashed #aaa}
.pager{display:flex;gap:10px}
.pager svg{width:8px;height:14px}
.video-frame{position:absolute;left:65px;top:652px;width:242px;height:151px;border:3px solid #c8c8c8;background:linear-gradient(180deg,#6d94c7 0%,#a9c2de 45%,#8c8f94 75%,#5d5f62 100%)}
.play-button{position:absolute;left:93px;top:36px}
.news-item{position:absolute;left:359px;width:256px;height:66px}
.news-item .thumb{position:absolute;left:0;top:0;width:103px;height:64px;border:2px solid #ccc}
.news-item h3{position:absolute;left:110px;top:2px;font-family:"Arimo",sans-serif;font-weight:400;font-size:11px;color:#111}
.news-item p{position:absolute;left:110px;top:17px;width:136px;font-size:7.4px;line-height:9.5px;color:#333;text-align:justify}
.news-meta{position:absolute;left:110px;top:53px;display:flex;gap:12px;font-size:6.6px;color:var(--link-blue)}
.news-meta span{display:flex;align-items:center;gap:2px}

/* corporate news */
.corporate{position:absolute;left:0;top:848px;width:714px;height:200px;background:var(--grey-band)}
.corporate-title{position:absolute;left:0;top:20px;width:714px;text-align:center;font-family:"Teko",sans-serif;font-size:22px;font-weight:400;color:#333;letter-spacing:.8px}
.corporate-rule{position:absolute;top:28px;height:6px;border-top:1px solid #999;border-bottom:1px solid #999}
.corp-item{position:absolute;top:78px;width:270px}
.corp-num{position:absolute;left:0;top:0;width:28px;height:27px;background:var(--white);border:1px solid #ccc;border-radius:3px;font-family:"Arimo",sans-serif;font-size:15px;color:var(--accent-red);text-align:center;line-height:26px;text-decoration:underline;text-underline-offset:2px}
.corp-item h3{position:absolute;left:35px;top:4px;width:240px;font-size:8.4px;line-height:11px;font-weight:700;color:#333;letter-spacing:.2px}
.corp-item p{position:absolute;left:35px;top:31px;width:250px;font-size:7.2px;line-height:10.8px;color:var(--muted)}
.corp-item a{position:absolute;left:35px;top:65px;font-size:7.6px;font-weight:700;color:#3c5c78;text-decoration:none}
.corp-divider{position:absolute;left:361px;top:64px;width:1px;height:100px;background:#cfcfcf}

/* footer */
.site-footer{position:absolute;left:0;top:1048px;width:714px;height:152px;background:var(--footer);border-top:5px solid var(--footer-rim)}
.footer-heading{position:absolute;top:20px;font-family:"Teko",sans-serif;font-weight:400;font-size:20px;color:var(--white)}
.testimonial{position:absolute;left:59px;top:52px;width:192px;font-size:8.4px;line-height:13.2px;color:var(--white);padding-left:15px}
.quote-open{position:absolute;left:0;top:0;font-family:Georgia,serif;font-size:16px;line-height:14px;color:#a9bfd0}
.quote-close{font-family:Georgia,serif;font-size:12px;line-height:10px;color:#a9bfd0;margin-left:4px}
.quick-links{position:absolute;left:282px;top:46px;list-style:none}
.quick-links li{font-size:8px;color:var(--white);line-height:16.6px;display:flex;align-items:center;gap:9px}
.quick-links li::before{content:"";width:3px;height:3px;border-radius:50%;background:#b9cddc}
.footer-brand{position:absolute;left:444px;top:54px;width:200px;display:flex;flex-direction:column;align-items:center;gap:8px}
.footer-brand .brand-mark{width:16px;height:16px;background:#dbe7ef}
.footer-brand .brand-name{font-size:19px;color:var(--white)}
.copyright{position:absolute;left:444px;top:118px;width:200px;text-align:center;font-size:6.6px;color:var(--white)}
</style>
</head>
<body>

<header class="site-header">
  <div class="brand">
    <span class="brand-mark"></span><span class="brand-name">corvalis immobilien</span>
  </div>
  <nav class="main-nav">
    <a class="is-current" href="#">HOME</a>
    <a href="#">ABOUT US</a>
    <a href="#">PROPERTIES</a>
    <a href="#">SERVICES &amp; NEWS</a>
    <a href="#">REFERENCES</a>
    <a href="#">CONTACT</a>
  </nav>
</header>

<section class="hero" role="img" aria-label="Curved glass office tower against a sunny blue sky">
  <div class="hero-caption">
    <h1>Real Estate Development and Brokerage company</h1>
    <p>simply dummy text of the printing and typesetting</p>
  </div>
</section>

<div class="audience-band"></div>

<article class="audience-card" style="left:60px">
  <h2>Institutional Investors</h2>
  <div class="thumb" role="img" aria-label="Curved residential complex with palm trees" style="background:linear-gradient(180deg,#4f6f93 0%,#9aa6ae 50%,#6b7a5d 100%)"></div>
  <p>Take advantage of our great deals on cruise packages.Save time and money with these special discounted offers by Harbor Line Tours. To reserve your package</p>
</article>
<article class="audience-card" style="left:266px">
  <h2>Wealthy Individuals</h2>
  <div class="thumb" role="img" aria-label="Modern building courtyard with a tree at dusk" style="background:linear-gradient(180deg,#3f5a75 0%,#7f8b5b 55%,#2f3a2a 100%)"></div>
  <p>Come aboard and discover the massive glaciers and amazing wildlife of the Kenai Fjords National Park discover the massive glaciers and amazing wildlife of the Kenai</p>
</article>
<article class="audience-card" style="left:476px">
  <h2>Family Offices</h2>
  <div class="thumb" role="img" aria-label="Row of modern townhouses at dusk" style="background:linear-gradient(180deg,#7e93b3 0%,#a8adb5 55%,#5d6e4a 100%)"></div>
  <p>Come aboard and discover the massive glaciers and amazing wildlife of the Kenai Fjords National Park discover the massive glaciers and amazing wildlife of the Kenai</p>
</article>

<h2 class="section-title abs" style="left:62px;top:612px">FEATURED VIDEOS</h2>
<div class="pager abs" style="left:286px;top:616px">
  <svg viewBox="0 0 8 14"><path d="M7 1 1 7l6 6" fill="none" stroke="#bbb" stroke-width="1.3"/></svg>
  <svg viewBox="0 0 8 14"><path d="M1 1l6 6-6 6" fill="none" stroke="#bbb" stroke-width="1.3"/></svg>
</div>
<div class="rule-dashed abs" style="left:62px;top:640px;width:256px"></div>
<div class="video-frame" role="img" aria-label="City street with modern office buildings">
  <svg class="play-button" width="56" height="56" viewBox="0 0 56 56"><circle cx="28" cy="28" r="26" fill="#1c1c1c" stroke="#e8e8e8" stroke-width="2"/><path d="M22 16v24l19-12z" fill="#fff"/></svg>
</div>

<h2 class="section-title abs" style="left:359px;top:612px">CORVALIS NEWS</h2>
<div class="pager abs" style="left:589px;top:616px">
  <svg viewBox="0 0 8 14"><path d="M7 1 1 7l6 6" fill="none" stroke="#bbb" stroke-width="1.3"/></svg>
  <svg viewBox="0 0 8 14"><path d="M1 1l6 6-6 6" fill="none" stroke="#bbb" stroke-width="1.3"/></svg>
</div>
<div class="rule-dashed abs" style="left:359px;top:640px;width:256px"></div>

<article class="news-item" style="top:651px">
  <div class="thumb" role="img" aria-label="Hand holding a small model house" style="background:linear-gradient(180deg,#3a6fb8 0%,#b8cbe0 55%,#9b7f63 100%)"></div>
  <h3>CAPTAIN'S BLOG</h3>
  <p>Calling all history buffs! Guests on our 3-Hour Resurrection Bay cruise on October special opportunity.</p>
  <div class="news-meta">
    <span><svg width="8" height="7" viewBox="0 0 8 7"><path d="M1 1h6v4H3L1 6.5z" fill="none" stroke="#1f4fa8" stroke-width=".8"/></svg>25 Comments</span>
    <span><svg width="7" height="7" viewBox="0 0 7 7"><rect x=".5" y="1" width="6" height="5.5" fill="#222"/></svg>Jan 21, 2015</span>
  </div>
</article>
<article class="news-item" style="top:738px">
  <div class="thumb" role="img" aria-label="Agent handing over keys to a client" style="background:linear-gradient(135deg,#6b5238 0%,#3a3a3a 50%,#2f5a3a 100%)"></div>
  <h3>CAPTAIN'S BLOG</h3>
  <p>Calling all history buffs! Guests on our 3-Hour Resurrection Bay cruise on October special opportunity.</p>
  <div class="news-meta">
    <span><svg width="8" height="7" viewBox="0 0 8 7"><path d="M1 1h6v4H3L1 6.5z" fill="none" stroke="#1f4fa8" stroke-width=".8"/></svg>25 Comments</span>
    <span><svg width="7" height="7" viewBox="0 0 7 7"><rect x=".5" y="1" width="6" height="5.5" fill="#222"/></svg>Jan 21, 2015</span>
  </div>
</article>

<section class="corporate">
  <div class="corporate-rule" style="left:72px;width:222px"></div>
  <div class="corporate-rule" style="left:432px;width:206px"></div>
  <h2 class="corporate-title">CORPORATE NEWS</h2>
  <div class="corp-divider"></div>
  <article class="corp-item" style="left:62px">
    <div class="corp-num">01</div>
    <h3>LOREM IPSUM DOLOR SIT AMET CONSECTETUR ADIPISICING</h3>
    <p>Sorrupti quos dolores etquas molestias exceptur sint occaecati cupificia deserunt mollitia animi id est laborum et dolorum fuga. Et harum quidem rerum facilisest et expedita distinctio.Sorrupti quos dolores etquas moles</p>
    <a href="#">read more...</a>
  </article>
  <article class="corp-item" style="left:371px;top:76px">
    <div class="corp-num">02</div>
    <h3>LOREM IPSUM DOLOR SIT AMET CONSECTETUR ADIPISICING</h3>
    <p>Sorrupti quos dolores etquas molestias exceptur sint occaecati cupificia deserunt mollitia animi id est laborum et dolorum fuga. Et harum quidem rerum facilisest et expedita distinctio.Sorrupti quos dolores etquas moles</p>
    <a href="#">read more...</a>
  </article>
</section>

<footer class="site-footer">
  <h2 class="footer-heading" style="left:59px">Testimonials</h2>
  <p class="testimonial"><span class="quote-open">&ldquo;</span>Video ads are free to create. Only pay to remove the watermark and download in high resolution when you're 100% satisfied with your ad. Once you've bought your ad, use it in the following places to increase sales and conversions<span class="quote-close">&rdquo;</span></p>

  <h2 class="footer-heading" style="left:279px">Quick Links</h2>
  <ul class="quick-links">
    <li>HOME</li>
    <li>ABOUT US</li>
    <li>PROPERTIES</li>
    <li>SERVICES &amp; NEWS</li>
    <li>REFERENCES</li>
    <li>CONTACT</li>
  </ul>

  <div class="footer-brand">
    <span class="brand-mark"></span>
    <span class="brand-name">corvalis immobilien</span>
  </div>
  <p class="copyright">© 2014 CORVALIS IMMOBILIEN, ALL RIGHTS RESERVED.</p>
</footer>

</body>
</html>
```